Website Re-Design

We would like to explore the possibility of a re-design of our website. We want all the content that it currently has to remain on the pages, and we don't want our logo/corporate identity or colours changed, so it is literally just a website re-design.

Our website is www.drelvix.co.uk

Websites that we like are

http://www.tarnwillow.co.uk/
http://quomplet.com/

```html
<!DOCTYPE html>
<html lang="en">
<head>
<meta charset="utf-8">
<title>Drelvix – Inbound Marketing &amp; SEO Performance Agency</title>
<link href="https://fonts.googleapis.com/css2?family=Oswald:wght@300;400&family=Raleway:wght@400;600;700&family=Open+Sans:wght@400;700&display=swap" rel="stylesheet">
<style>
:root{
  --pink:#e5007d;
  --teal:#00a99d;
  --teal-light:#5cc6bc;
  --lime:#8cc63f;
  --green:#86c046;
  --green-dark:#6ea936;
  --nav:#2b2b2b;
  --ink:#333;
  --ink-soft:#555;
  --grey-bg:#ececec;
  --white:#fff;
}
*{box-sizing:border-box;margin:0;padding:0}
html,body{width:1200px;height:3273px;overflow:hidden}
body{font-family:"Raleway",sans-serif;color:var(--ink);background:var(--white);position:relative}
section,header,footer{position:absolute;left:0;width:1200px}
.abs{position:absolute}
.center{text-align:center}

/* header */
.site-header{top:0;height:627px}
.hero-backdrop{position:absolute;inset:0;background:linear-gradient(180deg,#f4f5f6 0%,#e3e6e9 60%,#d4d8dc 100%)}
.topbar{position:absolute;top:0;left:0;width:1200px;height:76px;background:linear-gradient(180deg,rgba(40,40,40,.95),rgba(70,70,70,.9))}
.logo{position:absolute;left:142px;top:18px;font:700 38px "Raleway",sans-serif;color:var(--pink);letter-spacing:1px}
.main-nav{position:absolute;right:140px;top:25px;display:flex;gap:32px}
.main-nav a{font:700 19px "Open Sans",sans-serif;color:var(--white);text-decoration:none;letter-spacing:.5px}
.tile{position:absolute;color:var(--white);font:400 28px "Oswald",sans-serif;display:flex;align-items:flex-end;justify-content:center;padding-bottom:40px;letter-spacing:1px}
.tile-search{left:158px;top:169px;width:447px;height:357px;background:var(--pink)}
.tile-social{left:611px;top:245px;width:114px;height:200px;background:var(--lime);font-size:20px;padding-bottom:22px}
.tile-media{left:725px;top:245px;width:243px;height:314px;background:var(--teal)}

/* intro */
.intro{top:627px;height:251px}
.intro h1{font:300 38px "Oswald",sans-serif;color:var(--pink);line-height:1.15;margin-top:44px}
.intro p{width:820px;margin:28px auto 0;font-size:15px;line-height:1.5;color:var(--ink-soft)}

/* services */
.services{top:878px;height:546px;background:var(--teal);color:var(--white)}
.service{position:absolute;top:62px;width:292px;text-align:center}
.service h2{font:300 25px "Oswald",sans-serif;letter-spacing:.5px}
.service h2::after{content:"";display:block;width:46px;height:2px;background:rgba(255,255,255,.6);margin:16px auto 0}
.service .media{margin-top:22px;height:172px}
.service p{font-size:15px;line-height:1.45;margin:26px 10px 0}
.btn-more{display:inline-block;margin-top:22px;width:115px;height:30px;line-height:30px;background:var(--teal-light);color:var(--white);font:600 12px "Raleway",sans-serif;letter-spacing:1px;text-decoration:none}

/* works */
.works{top:1424px;height:589px;background:var(--grey-bg)}
.section-title{font:300 40px "Oswald",sans-serif;color:var(--pink);letter-spacing:.5px}
.works .section-title{margin-top:118px}
.works p,.clients p{width:800px;margin:14px auto 0;font-size:15px;line-height:1.5;color:var(--ink-soft)}
.work-shot{position:absolute;top:262px;height:185px;border:3px solid var(--white)}

/* clients */
.clients{top:2013px;height:354px;border-bottom:1px solid #e3e3e3}
.clients .section-title{margin-top:72px}
.client{position:absolute;top:191px;width:150px;height:109px;border:1px solid #ddd;display:flex;align-items:center;justify-content:center;font:700 19px "Raleway",sans-serif;color:#444;gap:8px}
.client .dot{width:14px;height:14px;border-radius:50%;background:#888}
.client.soon{font-size:17px;text-align:center;line-height:1.1}

/* call to action */
.cta{top:2367px;height:323px}
.cta h2{position:absolute;left:507px;top:58px;font:400 40px "Oswald",sans-serif;color:var(--pink);letter-spacing:1px}
.cta h3{position:absolute;left:507px;top:120px;font:700 25px "Open Sans",sans-serif;color:#222}
.cta p{position:absolute;left:507px;top:162px;width:560px;font-size:15px;line-height:1.5;color:var(--ink-soft)}
.btn-contact{position:absolute;left:507px;top:219px;width:161px;height:51px;line-height:51px;text-align:center;background:var(--teal);color:var(--white);font:700 16px "Open Sans",sans-serif;text-decoration:none;letter-spacing:.5px}

/* contact */
.contact{top:2690px;height:523px;background:var(--green);color:var(--white)}
.eyebrow{font:700 13px "Open Sans",sans-serif;letter-spacing:2px;margin-top:38px}
.contact h2{font:400 44px "Oswald",sans-serif;letter-spacing:4px;margin-top:10px}
.contact .lead{width:640px;margin:10px auto 0;font-size:14px;line-height:1.5}
.rule{position:absolute;left:142px;width:916px;height:1px;background:rgba(255,255,255,.45)}
.col{position:absolute;font-size:14px;line-height:1.55}
.col h4{font:700 13px "Open Sans",sans-serif;letter-spacing:1px;margin-bottom:10px}
.social{display:flex;gap:12px;font-size:13px;font-weight:700}
.links{list-style:none;font-size:13px;line-height:1.85}
.search-field{width:200px;height:32px;background:var(--white);color:#999;font-size:13px;padding:8px 10px;border-radius:3px}
.search-btn{display:inline-block;margin-top:10px;width:90px;height:30px;line-height:30px;text-align:center;background:var(--teal);font:700 12px "Open Sans",sans-serif;border-radius:3px}

/* footer */
.site-footer{top:3213px;height:60px;background:var(--green-dark);color:var(--white)}
.footer-logo{position:absolute;left:142px;top:13px;font:700 30px "Raleway",sans-serif;color:rgba(255,255,255,.55)}
.legal{position:absolute;left:302px;top:15px;font-size:11px;line-height:1.5}
</style>
</head>
<body>

<header class="site-header">
  <div class="hero-backdrop" role="img" aria-label="Web analytics dashboard screenshot with bar charts, softly blurred behind the tiles"></div>
  <div class="topbar">
    <div class="logo">DRELVIX</div>
    <nav class="main-nav">
      <a href="#">HOME</a><a href="#">ABOUT</a><a href="#">PORTFOLIO</a><a href="#">WHAT WE DO</a><a href="#">CONTACT US</a>
    </nav>
  </div>
  <div class="tile tile-search">SEARCH</div>
  <div class="tile tile-social">SOCIAL</div>
  <div class="tile tile-media">MEDIA</div>
</header>

<section class="intro center">
  <h1>DRELVIX<br>Your Inbound Marketing &amp; SEO Performance Agency</h1>
  <p>Do you want to earn your customers attention? Gain more visibility in the SERPs and build &amp; engage with your audience? Drelvix specialises in SEO, Social media, CRO and Design &amp; Creative services. Offering a bespoke and personal service from a team of digital natives.</p>
</section>

<section class="services">
  <div class="service" style="left:142px">
    <h2>What Can We Do For You?</h2>
    <div class="media" style="background:linear-gradient(135deg,#f7f7f7,#d9d9d9 60%,#e8449a)" role="img" aria-label="Laptop showing a pink bar chart"></div>
    <p>We offer a bespoke service and will customise to your needs. We specialise in progressive &amp; innovative solutions.</p>
    <a class="btn-more" href="#">READ MORE</a>
  </div>
  <div class="service" style="left:453px">
    <h2>See Our Portfolio</h2>
    <div class="media" style="background:linear-gradient(160deg,#ffffff,#eef3e4 60%,#9cc34a)" role="img" aria-label="Watering can pouring onto a young seedling"></div>
    <p>Take a look at our case-studies to see our recent campaigns showing results achieved for our clients.</p>
    <a class="btn-more" href="#">READ MORE</a>
  </div>
  <div class="service" style="left:766px">
    <h2>Let's Talk</h2>
    <div class="media" style="background:linear-gradient(160deg,#ffffff,#e6f4f3 55%,#3bb3b0)" role="img" aria-label="Turquoise retro rotary telephone"></div>
    <p>Use our form to send us a message, we will call you back as soon as we can.</p>
    <a class="btn-more" href="#">READ MORE</a>
  </div>
</section>

<section class="works center">
  <h2 class="section-title">RECENT WORKS</h2>
  <p>Check out our recent works and case-studies. These are a few examples to show the diversity of work that we can do to earn real attention, generate inbound links, mentions, citations and be used across many of our marketing channels. See more on our portfolio page and learn about what we could do for you.</p>
  <div class="work-shot" style="left:131px;width:311px;background:linear-gradient(135deg,#5ec3ea,#e9eef2 55%,#b8c4cc)" role="img" aria-label="Website project shown on laptop and monitor screens"></div>
  <div class="work-shot" style="left:447px;width:300px;background:linear-gradient(135deg,#e8e8e8,#7a7f86 50%,#cfd2d6)" role="img" aria-label="Website project shown on a desktop monitor with screenshot panels"></div>
  <div class="work-shot" style="left:758px;width:303px;background:linear-gradient(135deg,#e8449a,#f3c1d9 45%,#5a6fa0)" role="img" aria-label="Infographic campaign panels on a pink background"></div>
</section>

<section class="clients center">
  <h2 class="section-title">OUR CLIENTS</h2>
  <p>We work with and represent a number of progressive companies in their SEO, social, inbound marketing, content and strategy needs. Check out our case-studies for examples.</p>
  <div class="client" style="left:155px"><span class="dot"></span>Parlwick</div>
  <div class="client" style="left:338px">Tutorvane</div>
  <div class="client" style="left:521px">Vantrel</div>
  <div class="client" style="left:714px">Staylorn</div>
  <div class="client soon" style="left:900px">Image<br>coming<br>soon</div>
</section>

<section class="cta">
  <div class="abs" style="left:142px;top:47px;width:316px;height:231px;background:radial-gradient(ellipse at 50% 75%,#f2c9a8,#fbeee4 55%,#ffffff 80%)" role="img" aria-label="Hand-drawn speech bubbles above raised fingers"></div>
  <h2>SOUND INTERESTING?</h2>
  <h3>Interested in what you have seen so far?</h3>
  <p>Are you looking for a progressive and innovative inbound marketing agency who can work alongside your existing teams. If Yes, then let's have a chat.</p>
  <a class="btn-contact" href="#">CONTACT US</a>
</section>

<section class="contact center">
  <div class="eyebrow">CONTACT</div>
  <h2>WHERE ARE WE?</h2>
  <p class="lead">We are in London, UK, based down the best mews in Little Venice, so come check it out and walk the canals with us or we're happy to venture to you!</p>
  <div class="rule" style="top:196px"></div>
  <div class="col" style="left:142px;top:215px;text-align:left">
    <h4>UK OFFICE</h4>27 Calloway Mews, Little Venice,<br>London, UK, W9 4QT
  </div>
  <div class="col" style="left:398px;top:215px;text-align:left">
    <h4>PHONE</h4><span style="font-size:18px">+44 (0) 207 946 0321</span>
  </div>
  <div class="col" style="left:627px;top:215px;text-align:left">
    <h4>EMAIL</h4><span style="font-size:17px">hello@drelvix.co.uk</span>
  </div>
  <div class="col" style="left:856px;top:215px;text-align:left">
    <h4>CONNECT WITH US</h4>
    <div class="social"><span>Chatter</span><span>Plusly</span><span>Linkvo</span></div>
  </div>
  <div class="rule" style="top:310px"></div>
  <div class="col" style="left:142px;top:332px;text-align:left">
    <h4>USEFUL LINKS</h4>
    <ul class="links"><li>HOME</li><li>ABOUT</li><li>PORTFOLIO</li><li>WHAT WE DO</li><li>CONTACT US</li></ul>
  </div>
  <div class="col" style="left:398px;top:332px;width:400px;text-align:left;font-size:13px">
    <h4>ABOUT US</h4>
    Drelvix is an inbound marketing agency offering a raft of services from digital strategy and planning through to SEO, Social media, SMM, CRO, Design &amp; Creative, through to paid for performance campaigns.<br><br>Talk to us to discuss your needs.
  </div>
  <div class="col" style="left:856px;top:332px;text-align:left">
    <h4>SEARCH THIS SITE</h4>
    <div class="search-field">Search</div>
    <div class="search-btn">SEARCH</div>
  </div>
</section>

<footer class="site-footer">
  <div class="footer-logo">DRELVIX</div>
  <div class="legal"><strong>COPYRIGHT (C) 2013 DRELVIX. ALL RIGHTS RESERVED.</strong><br>Drelvix is the trading name of Drelvix Limited, registered in the UK at Companies House 09384415, and VAT registered 318 4472 90.</div>
</footer>

</body>
</html>
```